Business Card Design

I need a business card for my company i am starting. I will be providing stump grinding services. I use a motorized machine to grind stumps down under the ground so that they are out of the way and out of sight. I'm looking for my card to have maroon or dark red somewhere in the card to match my truck. I'm going to use this card to advertise and also serve as a design to wrap my truck tailgate as advertisement so i want it to match. the dark maroon color of my truck. I wouldn't mind using bright colors or color for the rest of the card or the lettering or any designs on the card. In the images i have provided i like how there are saw blades integrated into these people advertisements. I also like the illustration of the stump grinder. I also provided a picture of the actual cutting wheel or blade of the grinder.

Industry/Entity Type

Business

Contact Information for Business Card

Company Name - Oakline Stump Grinding
Phone - 407-219-5573
Email - harlow.stumpwork@quillpost.net
Name and title - Thomas Harlow - Owner and operator
Company Slogan - Ground down, out of sight

```html
<!DOCTYPE html>
<html lang="en">
<head>
<meta charset="utf-8">
<title>Oakline Stump Grinding – Business Card</title>
<link rel="stylesheet" href="https://fonts.googleapis.com/css2?family=Open+Sans:wght@400;600;700;800&display=swap">
<style>
  :root {
    --backdrop: #1c1c1c;
    --card-white: #ffffff;
    --brand-red: #b01e23;
    --brand-red-light: #c0302f;
    --brand-red-dark: #9c1a1e;
    --ink: #1e1e1e;
    --ink-soft: #2b2b2b;
  }
  * { box-sizing: border-box; margin: 0; padding: 0; }
  html, body {
    width: 1200px; height: 900px; overflow: hidden;
    background: var(--backdrop);
    font-family: "Open Sans", Arial, sans-serif;
  }
  .canvas { position: relative; width: 1200px; height: 900px; }

  .card {
    position: absolute; top: 170px;
    width: 347px; height: 561px;
  }
  .card--front { left: 259px; background: var(--card-white); }
  .card--back {
    left: 631px;
    background: linear-gradient(180deg, var(--brand-red-light) 0%, var(--brand-red-dark) 100%);
  }

  .tab {
    position: absolute; left: 102px; width: 143px; height: 30px;
    background: linear-gradient(180deg, var(--brand-red-light), var(--brand-red-dark));
  }
  .tab--top { top: 0; }
  .tab--bottom { bottom: 0; }

  .brand {
    position: absolute; top: 143px; left: 35px; right: 26px;
    display: flex; align-items: center; gap: 12px;
  }
  .brand__dot {
    flex: 0 0 auto; width: 80px; height: 80px; border-radius: 50%;
    background: var(--brand-red);
  }
  .brand__text { display: flex; flex-direction: column; }
  .brand__name {
    font-weight: 700; font-size: 21px; line-height: 25px;
    color: var(--brand-red); text-transform: uppercase; letter-spacing: 0.3px;
  }
  .brand__slogan {
    margin-top: 4px; font-weight: 700; font-size: 11.5px; color: var(--ink);
  }

  .person {
    position: absolute; top: 285px; left: 0; right: 0; text-align: center;
  }
  .person__name { font-weight: 600; font-size: 19px; color: var(--brand-red); line-height: 24px; }
  .person__title { font-size: 14.5px; color: var(--ink-soft); line-height: 20px; }

  .contact {
    position: absolute; top: 357px; left: 0; right: 0;
    display: flex; flex-direction: column; align-items: center; gap: 4px;
    font-size: 15px; color: var(--ink);
  }
  .contact__row { display: flex; align-items: center; gap: 8px; line-height: 20px; }
  .contact__icon { width: 12px; height: 12px; fill: var(--brand-red); }
</style>
</head>
<body>
<main class="canvas">
  <section class="card card--front" aria-label="Business card front">
    <div class="tab tab--top"></div>

    <div class="brand">
      <span class="brand__dot"></span>
      <div class="brand__text">
        <span class="brand__name">Oakline Stump<br>Grinding</span>
        <span class="brand__slogan">Ground down, out of sight</span>
      </div>
    </div>

    <div class="person">
      <p class="person__name">Thomas Harlow</p>
      <p class="person__title">Owner &amp; Operator</p>
    </div>

    <div class="contact">
      <p class="contact__row">
        <svg class="contact__icon" viewBox="0 0 24 24" aria-hidden="true">
          <path d="M6.6 10.8a15.1 15.1 0 0 0 6.6 6.6l2.2-2.2a1 1 0 0 1 1-.25 11.4 11.4 0 0 0 3.6.57 1 1 0 0 1 1 1V20a1 1 0 0 1-1 1A17 17 0 0 1 3 4a1 1 0 0 1 1-1h3.5a1 1 0 0 1 1 1c0 1.25.2 2.45.57 3.6a1 1 0 0 1-.25 1z"/>
        </svg>
        <span>407-219-5573</span>
      </p>
      <p class="contact__row">
        <svg class="contact__icon" viewBox="0 0 24 24" aria-hidden="true">
          <path d="M2 5h20v14H2zM3.5 6.5 12 13l8.5-6.5z" fill-rule="evenodd"/>
        </svg>
        <span>harlow.stumpwork@quillpost.net</span>
      </p>
    </div>

    <div class="tab tab--bottom"></div>
  </section>

  <section class="card card--back" role="img" aria-label="Card back in deep red with a large embossed brand decoration"></section>
</main>
</body>
</html>
```